HPS business cards

(Generators . Lighting Towers . De-watering Pumps . Compressors) put under the logo please. my details are Owen Pritchard (Director) 0461527390 harbourpinesupply@postvale.net

```html
<!DOCTYPE html>
<html lang="en">
<head>
<meta charset="utf-8">
<title>HPS business cards</title>
<link href="https://fonts.googleapis.com/css2?family=Poppins:wght@400;500;600;700&display=swap" rel="stylesheet">
<style>
  :root {
    --stage: #2b2c2f;
    --card-light: #ffffff;
    --card-dark: #262629;
    --gold: #f0a630;
    --gold-deep: #cf7f22;
    --silver: #b9b9bb;
    --silver-light: #e6e6e7;
    --ink-grey: #7a7a7c;
    --white: #ffffff;
  }
  * { margin: 0; padding: 0; box-sizing: border-box; }
  html, body { width: 1200px; height: 952px; overflow: hidden; }
  body {
    background: var(--stage);
    font-family: "Poppins", sans-serif;
    display: flex;
    align-items: center;
    justify-content: center;
    gap: 40px;
  }
  .card {
    position: relative;
    width: 540px;
    height: 309px;
    overflow: hidden;
    box-shadow: 0 18px 40px rgba(0,0,0,.45);
  }
  .card--front { background: var(--card-light); }
  .card--back { background: var(--card-dark); }

  .card__band {
    position: absolute;
    left: 0; bottom: 0;
    width: 540px; height: 40px;
  }

  .brand {
    position: absolute;
    left: 0; right: 0;
    display: flex;
    align-items: center;
    justify-content: center;
    gap: 12px;
  }
  .brand__square {
    width: 26px; height: 26px;
    border: 3px solid var(--gold);
  }
  .brand__name {
    font-weight: 600;
    font-size: 26px;
    letter-spacing: .5px;
    color: var(--gold);
    text-transform: uppercase;
  }
  .card--front .brand { top: 72px; }
  .card--back .brand { top: 92px; }

  .person {
    position: absolute;
    top: 150px;
    right: 330px;
    text-align: right;
  }
  .person__name {
    font-weight: 700;
    font-size: 19px;
    color: var(--gold);
    line-height: 1.2;
  }
  .person__role {
    font-size: 12px;
    color: var(--ink-grey);
  }
  .contacts {
    position: absolute;
    top: 152px;
    left: 224px;
    list-style: none;
  }
  .contacts__item {
    display: flex;
    align-items: center;
    gap: 8px;
    font-size: 12.5px;
    color: var(--ink-grey);
    margin-bottom: 8px;
  }
  .contacts__icon {
    width: 18px; height: 18px;
    border-radius: 3px;
    background: var(--gold);
    display: flex; align-items: center; justify-content: center;
  }

  .services {
    position: absolute;
    top: 146px;
    left: 0; right: 0;
    text-align: center;
    color: var(--white);
    font-weight: 500;
    font-size: 12px;
    letter-spacing: .3px;
    line-height: 1.8;
    text-transform: uppercase;
  }
  .services__dot { color: var(--gold); margin: 0 4px 0 10px; }
</style>
</head>
<body>
  <svg width="0" height="0" style="position:absolute">
    <defs>
      <linearGradient id="goldBand" x1="0" x2="1" y1="0" y2="0">
        <stop offset="0" stop-color="#f6b444"/>
        <stop offset=".45" stop-color="#cf7f22"/>
        <stop offset="1" stop-color="#f4ac3a"/>
      </linearGradient>
      <linearGradient id="silverBand" x1="0" x2="1" y1="0" y2="0">
        <stop offset="0" stop-color="#e6e6e7"/>
        <stop offset="1" stop-color="#9d9d9f"/>
      </linearGradient>
    </defs>
  </svg>

  <section class="card card--front">
    <div class="brand">
      <span class="brand__square"></span>
      <span class="brand__name">Harbour Pine Supply</span>
    </div>

    <div class="person">
      <p class="person__name">Owen Pritchard</p>
      <p class="person__role">Director</p>
    </div>

    <ul class="contacts">
      <li class="contacts__item">
        <span class="contacts__icon">
          <svg width="11" height="11" viewBox="0 0 24 24"><path fill="#fff" d="M6.6 10.8a15 15 0 0 0 6.6 6.6l2.2-2.2c.3-.3.7-.4 1-.2 1.1.4 2.3.6 3.6.6.6 0 1 .4 1 1V20c0 .6-.4 1-1 1A17 17 0 0 1 3 4c0-.6.4-1 1-1h3.5c.6 0 1 .4 1 1 0 1.3.2 2.5.6 3.6.1.3 0 .7-.2 1z"/></svg>
        </span>
        0461527390
      </li>
      <li class="contacts__item">
        <span class="contacts__icon">
          <svg width="11" height="11" viewBox="0 0 24 24"><rect x="2" y="5" width="20" height="14" fill="none" stroke="#fff" stroke-width="2"/><path d="M2 5l10 8 10-8" fill="none" stroke="#fff" stroke-width="2"/></svg>
        </span>
        harbourpinesupply@postvale.net
      </li>
    </ul>

    <svg class="card__band" viewBox="0 0 540 40" aria-hidden="true">
      <polygon points="0,30 150,30 150,40 0,40" fill="url(#silverBand)"/>
      <polygon points="150,14 540,14 540,40 130,40" fill="url(#goldBand)"/>
    </svg>
  </section>

  <section class="card card--back">
    <div class="brand">
      <span class="brand__square"></span>
      <span class="brand__name">Harbour Pine Supply</span>
    </div>

    <p class="services">
      <span class="services__dot">•</span>Generators
      <span class="services__dot">•</span>Lighting Towers
      <span class="services__dot">•</span>De-watering Pumps<br>
      <span class="services__dot">•</span>Compressors
    </p>

    <svg class="card__band" viewBox="0 0 540 40" aria-hidden="true">
      <polygon points="0,30 150,30 150,40 0,40" fill="url(#silverBand)"/>
      <polygon points="150,14 540,14 540,40 130,40" fill="url(#goldBand)"/>
    </svg>
  </section>
</body>
</html>
```